依頼詳細
レスポンシブウェブデザインを意識したデザインでお願いします。

デザインに関しては、添付してあるデザインレイアウトシートを基にお願いします。
参考サイトのURLはデザインレイアウトシートに記載してあります。
色合いはグリーンかブルーを基調にお願いします。
新規のウェブサイトですので、既存サイトはありません。
ロゴも不要です。(後ではめ込むので社名だけテキストでレイアウトをお願いします。)
また、写真データも添付するので、レイアウトシートのイメージ画像に当て込んでください。

まずはパソコンサイトのデザインをお願いします。
当選後、スマホデザインをお願いします。

既存のテンプレートを使う場合は
テンプレート名を下記のような記載を提案の中にいれてください。
例:WordpressテーマはCorpLumen、デザインスキンは無料のQRN2019 LX4(http://corplumen.example/ex_plugin/qrnfuji2019_lx4/)をベースにデザインいたしました。
など

写真データで足りない場合は、一旦他のサイトや参考URLの写真をサンプルとして入れてください。(サンプルなどの表記をお願いします)
また、購入が必要な写真などを利用した場合は、Pixora Stock(https://stock.pixora-img.example/jp/)からファイル番号と価格を教えてください。
ページ数
1ページ
希望イメージ
シンプル 複雑
単色 カラフル
暗い 明るい
日常 高級
遊び心 厳粛
未来的 伝統的
女性的 男性的
希望する色
青系、緑系
納品ファイル
• イラストレーター形式 (.ai)
• フォトショップ形式 (.psd)
• PNG形式 (.png)
補足説明
上記のいずれか1つ。アウトラインありとなしの2つ。

こちらの要望を汲んで、デザインしていただきました。
ありがとうございました。

たくさんのご提案ありがとうございました。
次回もぜひ、よろしくお願い致します。

```html
<!DOCTYPE html>
<html lang="ja">
<head>
<meta charset="utf-8">
<title>株式会社 翠工</title>
<link href="https://fonts.googleapis.com/css2?family=Noto+Sans+JP:wght@400;500;700;900&family=Roboto:wght@400;700&display=swap" rel="stylesheet">
<style>
:root{
  --green:#3da53a;
  --green-dark:#2b7f2a;
  --text:#333;
  --muted:#777;
  --line:#ddd;
  --gray-bg:#f2f3f4;
  --sky-top:#3f7fc9;
  --sky-bottom:#cfe3f5;
  --white:#fff;
}
*{margin:0;padding:0;box-sizing:border-box}
html,body{width:1200px;height:2908px;overflow:hidden}
body{font-family:"Noto Sans JP",sans-serif;color:var(--text);background:var(--white);position:relative}
a{text-decoration:none}
.en{font-family:"Roboto",sans-serif}

/* header */
.site-header{position:absolute;top:0;left:0;width:1200px;height:72px;z-index:5}
.brand{position:absolute;left:244px;top:22px;color:var(--white);font-weight:700;font-size:16px;letter-spacing:1px;white-space:nowrap}
.global-nav{position:absolute;left:620px;top:0;display:flex;height:62px}
.global-nav a{width:72px;color:var(--white);font-size:11px;font-weight:700;text-align:center;padding-top:18px;line-height:1.3;white-space:nowrap}
.global-nav a span{display:block;font-size:8px;font-weight:400;opacity:.85}
.global-nav a.nav-contact{background:var(--green);width:84px;height:62px}

/* hero */
.hero{position:absolute;top:0;left:0;width:1200px;height:560px;background:linear-gradient(180deg,var(--sky-top) 0%,#6ea6dc 45%,var(--sky-bottom) 100%)}
.hero-copy{position:absolute;left:236px;top:250px}
.hero-copy p{display:inline-block;background:rgba(20,60,120,.55);color:var(--white);font-size:34px;font-weight:900;letter-spacing:3px;padding:2px 10px;margin-bottom:10px}

/* section heads */
.sec-label{color:var(--green);font-size:11px;font-weight:700;font-style:normal}
.sec-title{font-size:24px;font-weight:700;margin:4px 0 8px}
.sec-lead{font-size:13px;font-weight:700}
.btn-more{display:inline-block;background:var(--green);color:var(--white);font-size:11px;font-weight:700;width:104px;height:26px;line-height:26px;padding-left:14px;position:relative}
.btn-more::after{content:"";position:absolute;right:10px;top:10px;border-left:6px solid var(--white);border-top:3px solid transparent;border-bottom:3px solid transparent}

/* features */
.features{position:absolute;top:580px;left:0;width:1200px;height:400px;background:var(--white)}
.features-photo{position:absolute;right:0;top:0;width:740px;height:400px;background:linear-gradient(135deg,#c9d3dc,#8f9ba6 60%,#6b7580);clip-path:polygon(22% 0,100% 0,100% 100%,0 100%)}
.features-text{position:absolute;left:236px;top:60px;width:280px}
.features-text .sec-title{border-left:4px solid var(--green);padding-left:8px}
.features .btn-more{position:absolute;left:236px;top:278px}

/* services */
.services{position:absolute;top:1020px;left:0;width:1200px;height:720px}
.services-head{text-align:center;padding-top:40px}
.services-desc{width:740px;margin:14px auto 0;font-size:11px;line-height:1.9;color:var(--muted);text-align:center}
.service-grid{position:absolute;top:170px;left:272px;width:656px;display:grid;grid-template-columns:repeat(3,208px);column-gap:16px;row-gap:44px}
.service-card .thumb{height:156px;background:linear-gradient(160deg,#b7c3cc,#7d8a96)}
.service-card .thumb.warm{background:linear-gradient(160deg,#c7c1b4,#8f8a80)}
.service-card h3{font-size:12px;font-weight:700;margin:8px 0 4px;display:flex;align-items:center;gap:6px}
.service-card h3::before{content:"";width:8px;height:8px;background:var(--green)}
.service-card p{font-size:10px;line-height:1.7;color:var(--muted)}

/* recruit */
.recruit{position:absolute;top:1760px;left:0;width:1200px;height:420px;background:var(--gray-bg)}
.recruit-photo{position:absolute;left:0;top:0;width:700px;height:420px;background:linear-gradient(120deg,#d8dde2,#a8b4bf 55%,#e6e9ec);clip-path:polygon(0 0,100% 0,78% 100%,0 100%)}
.recruit-text{position:absolute;left:644px;top:100px}
.recruit .btn-more{position:absolute;left:924px;top:290px}

/* information */
.info{position:absolute;top:2220px;left:280px;width:640px}
.info-head{display:flex;align-items:baseline;gap:8px;border-bottom:2px solid var(--green);padding-bottom:6px}
.info-head h2{font-size:18px;font-weight:700}
.info-head span{font-size:10px;color:var(--muted)}
.info-list{list-style:none}
.info-list li{display:flex;align-items:center;gap:12px;font-size:11px;height:30px;border-bottom:1px solid var(--line)}
.info-list time{color:var(--muted);width:70px}
.info-list .tag{background:var(--green);color:var(--white);font-size:9px;width:58px;text-align:center;padding:2px 0}
.info-list .tag.alt{background:#c94a4a}

/* contact */
.contact{position:absolute;top:2440px;left:0;width:1200px;height:320px;background:var(--gray-bg)}
.contact-photo{position:absolute;left:196px;top:6px;width:250px;height:314px;background:linear-gradient(180deg,#e9e4de,#cfd6dc);border-radius:4px}
.contact-head{position:absolute;left:460px;top:48px;width:560px;text-align:center}
.contact-head .sec-label{display:block}
.contact-head h2{font-size:24px;font-weight:700}
.contact-head p{font-size:11px;color:var(--muted);margin-top:8px}
.contact-hours{position:absolute;left:500px;top:170px;width:160px;height:64px;background:var(--green);color:var(--white);font-size:11px;font-weight:700;padding:12px 14px;line-height:1.6}
.contact-tel{position:absolute;left:676px;top:174px;display:flex;align-items:center;gap:6px;color:var(--green-dark);font-size:22px;font-weight:700;white-space:nowrap}
.contact-tel-note{position:absolute;left:680px;top:206px;font-size:10px;color:var(--muted);white-space:nowrap}
.contact-mail{position:absolute;left:886px;top:176px;width:220px;height:46px;background:var(--green);color:var(--white);font-size:11px;font-weight:700;display:flex;align-items:center;justify-content:center;gap:8px;white-space:nowrap}

/* footer */
.site-footer{position:absolute;top:2760px;left:0;width:1200px;height:148px}
.footer-brand{position:absolute;left:196px;top:36px}
.footer-brand .name{font-size:16px;font-weight:700;letter-spacing:1px}
.footer-brand p{font-size:10px;color:var(--muted);line-height:1.7;margin-top:4px}
.footer-nav{position:absolute;left:700px;top:36px;display:grid;grid-template-columns:repeat(3,110px);row-gap:8px}
.footer-nav a{font-size:10px;color:var(--text);display:flex;align-items:center;gap:6px;white-space:nowrap}
.footer-nav a::before{content:"";width:6px;height:6px;background:var(--green)}
.copyright{position:absolute;bottom:0;left:0;width:1200px;height:26px;background:var(--green-dark);color:var(--white);font-size:9px;text-align:center;line-height:26px}
</style>
</head>
<body>

<header class="site-header">
  <div class="brand">株式会社 翠工</div>
  <nav class="global-nav">
    <a href="#">ホーム<span>HOME</span></a>
    <a href="#">当社の特徴<span>FEATURE</span></a>
    <a href="#">業務内容<span>SERVICE</span></a>
    <a href="#">会社概要<span>COMPANY</span></a>
    <a href="#">採用情報<span>RECRUIT</span></a>
    <a href="#" class="nav-contact">お問い合わせ<span>CONTACT</span></a>
  </nav>
</header>

<section class="hero" role="img" aria-label="青空の下、クレーンが立つ建設中のビルの写真">
  <div class="hero-copy">
    <p>建設現場の安全と</p><br>
    <p>環境づくりをサポート</p>
  </div>
</section>

<section class="features">
  <div class="features-photo" role="img" aria-label="資材置き場に積まれた足場材の写真"></div>
  <div class="features-text">
    <em class="sec-label en">Our Feature</em>
    <h2 class="sec-title">当社の特徴</h2>
    <p class="sec-lead">建設現場の安全環境をトータルサポート</p>
  </div>
  <a href="#" class="btn-more en">VIEW MORE</a>
</section>

<section class="services">
  <div class="services-head">
    <em class="sec-label en">Service</em>
    <h2 class="sec-title">業務内容</h2>
    <p class="services-desc">足場材のレンタルから搬入・組立・点検まで、現場の安全を支えるサービスを幅広くご提供しています。<br>地域の建設現場に寄り添い、迅速で確かな対応をお約束いたします。</p>
  </div>
  <div class="service-grid">
    <article class="service-card"><div class="thumb" role="img" aria-label="積み上げられた足場材の写真"></div><h3>タイトル</h3><p>テキストが入ります。足場材の管理と点検を丁寧に行い安全な現場をつくります。</p></article>
    <article class="service-card"><div class="thumb" role="img" aria-label="資材ヤードの写真"></div><h3>タイトル</h3><p>テキストが入ります。現場に合わせた資材を迅速にお届けし工期を支えます。</p></article>
    <article class="service-card"><div class="thumb warm" role="img" aria-label="作業中のスタッフの写真"></div><h3>タイトル</h3><p>テキストが入ります。経験豊富なスタッフが組立から解体まで対応します。</p></article>
    <article class="service-card"><div class="thumb warm" role="img" aria-label="倉庫内で作業するスタッフの写真"></div><h3>タイトル</h3><p>テキストが入ります。倉庫での整備と保管体制で品質を保っています。</p></article>
    <article class="service-card"><div class="thumb" role="img" aria-label="洗浄された資材の写真"></div><h3>タイトル</h3><p>テキストが入ります。使用後の資材は洗浄と補修を行い再利用します。</p></article>
    <article class="service-card"><div class="thumb" role="img" aria-label="工場内の設備の写真"></div><h3>タイトル</h3><p>テキストが入ります。自社設備により安定した供給体制を整えています。</p></article>
  </div>
</section>

<section class="recruit">
  <div class="recruit-photo" role="img" aria-label="ヘルメット姿の作業員が現場で打ち合わせをする写真"></div>
  <div class="recruit-text">
    <em class="sec-label en">Recruit</em>
    <h2 class="sec-title">採用情報</h2>
    <p class="sec-lead">建設現場の安全環境をトータルサポート</p>
  </div>
  <a href="#" class="btn-more en">VIEW MORE</a>
</section>

<section class="info">
  <div class="info-head"><h2 class="en">Information</h2><span>お知らせ</span></div>
  <ul class="info-list">
    <li><time class="en">2019.00.00</time><span class="tag alt">お知らせ</span>ホームページを公開いたしました。</li>
    <li><time class="en">2019.00.00</time><span class="tag">採用情報</span>スタッフの募集を開始いたしました。</li>
    <li><time class="en">2019.00.00</time><span class="tag">お知らせ</span>夏季休業期間のご案内です。</li>
  </ul>
</section>

<section class="contact">
  <div class="contact-photo" role="img" aria-label="受付スタッフの女性の写真"></div>
  <div class="contact-head">
    <em class="sec-label en">Contact</em>
    <h2>お問い合わせ</h2>
    <p>ご質問・ご相談などお気軽にお問い合わせください。</p>
  </div>
  <div class="contact-hours">受付時間<br>平日 8:00〜17:00</div>
  <div class="contact-tel en">
    <svg width="20" height="20" viewBox="0 0 24 24"><path fill="#2b7f2a" d="M6.6 10.8a15 15 0 0 0 6.6 6.6l2.2-2.2c.3-.3.7-.4 1-.2 1.1.4 2.3.6 3.6.6.6 0 1 .4 1 1V20c0 .6-.4 1-1 1A17 17 0 0 1 3 4c0-.6.4-1 1-1h3.5c.6 0 1 .4 1 1 0 1.3.2 2.5.6 3.6.1.3 0 .7-.2 1z"/></svg>
    012-345-6789
  </div>
  <p class="contact-tel-note">お電話でのお問い合わせはこちら</p>
  <a href="#" class="contact-mail">
    <svg width="16" height="12" viewBox="0 0 16 12"><rect x="0.5" y="0.5" width="15" height="11" fill="none" stroke="#fff"/><path d="M1 1l7 6 7-6" fill="none" stroke="#fff"/></svg>
    メールでのお問い合わせはこちら
  </a>
</section>

<footer class="site-footer">
  <div class="footer-brand">
    <div class="name">株式会社 翠工</div>
    <p>〒000-0000 〇〇県〇〇市〇〇町0-0-0<br>TEL 012-345-6789</p>
  </div>
  <nav class="footer-nav">
    <a href="#">ホーム</a><a href="#">会社概要</a><a href="#">お問い合わせ</a>
    <a href="#">当社の特徴</a><a href="#">採用情報</a><a href="#">プライバシー</a>
    <a href="#">業務内容</a><a href="#">お知らせ</a>
  </nav>
  <div class="copyright en">Copyright © Suikou Co., Ltd. All Rights Reserved.</div>
</footer>

</body>
</html>
```